Product presentation and placement brochure

I have cardiovascular exercise equipment (treadmill, bikes, eliptical trainers, etc.) that have a coin timers attached that allow use of this exercise equipment using coins. I want to market to apartment buildings, swimming pools, training gyms, etc. We want them to partner with us by allowing us to place our equipment in their locations. Their residents would get new equipment to use, they use a coin to get so much time. The apartment building doesn't pay anything precharge us workspace, but they will get a 10 - 20% of all the revenue that flows through the machines in their building.This brochure needs to clearly display our equipment, how the residents can use it, the ease of the relationship between us and the apartment building, and how they will make money with no investment and no commitment.I would, like the brochure to look artistic, not so mechanical.

Target Market(s)

Large apartment buildings, Public swimming pools, training studios, gyms, etc.

Font styles to use
Serif

Colors

Designer to choose colors to be used in the design.

Requirements
Must have
• The basic wording for the brochure. Must have English and Chinese.
• Vero Pulse Machine Brochure
• 維諾脈動健身器材指南
• We will pay YOU to let us provide YOU with commercial cardiovascular equipment.
• 我們付你錢來讓我們提供你有氧器材
• We supply cardio equipment to your residents at no cost to you. In fact, we will pay you! Please take a moment to look at our brochure and see how we can work with you and your homeowners association to bring the latest in fitness technology to your building, and we’ll pay you for it.
• 在不花費你任何金錢的情況下, 我們提供有氧器材給你的住戶。甚至我們付你錢!請看我們的手冊來了解我們如何能和你跟社區管理委員會合作, 把最新的健身器材介紹到你的大樓, 並且帶給你收益。
• Our machines are all equipped with patented coin operated technology. If your residents would like to have the luxury of quality exercise, they may insert dollars for minutes.
• 我們的器材皆具備專利通過投幣式設計。如果你的住戶想要享有高品質運動, 他們可以投幣來取得運動時間。
• By the 10th of every month, we will pay 15% of all revenue collected for the previous month, minus taxes, to you or your homeowners association, whichever you choose.
• 每個月10號, 我們將付你或社區管理委員會前一個月百分之十五不含稅的收入。
• Why it is so easy:
• 1. We provide the equipment at no cost to you.
• 2. We pay for shipping and installation.
• 3. Month-to-month agreement, no commitment from you.
• 4. Removal with 30 days notice, no questions asked.
• 5. We conduct all repairs and regular maintenance.
• 6. We will pay you from the revenue collected!
• 為什麼超簡單:
• 1. 不花你一毛錢, 器材我們提供。
• 2. 運送費跟安裝費, 全數我們支付。
• 3. 以一個月為一期, 不用長期保證。
• 4. 30天移出通知, 不需任何理由。
• 5. 所有器材維修, 我們負責。
• 6. 器材收益,我們分享!
• As easy as 1, 2, 3!
• 簡單有如1, 2, 3!
• STEP 1
• We have several different machine types that will motivate your residents to exercise:
• 1. Treadmill (photo and stats.)
• 2. Recumbent Bike (photo and stats.)
• 3. Regular Seated Bike (photo and stats.)
• 4. Elliptical trainer (photo and stats.)
• Replace old equipment, broken equipment, or just place new equipment next to your old equipment.
• 第一步
• 我們有多種有氧器材可讓住戶更有動力運動:
• 1. 跑步機
• 2. 臥式腳踏車
• 3. 直立式腳踏車
• 4. 橢圓機
• 替換原有老舊的運動器材, 或是直接放一台新的器材在原有器材的旁邊。
• After meeting with you and determining you and your residents needs, we will decide how many and of what types of equipment you would like in your exercise room.
• 在和你會面並且評估你和住戶的需求後, 我們會決定你想要的器材種類和數量。
• STEP 2
• We will deliver and install the equipment, in a suitable location that you choose. All at no cost to you!
• 第二步
• 我們將器材運送到你選擇的合適場所並安裝。不需任何費用!
• Step 3
• 第三步
• Make your residents healthy and happy by letting them use any of the equipment, for as long as they like, at their leisure.
• 住戶可盡情使用任何器材, 讓住戶健康又開心。
• Photo Steps on how to use equipment
• 0. 2. 3.
• We would be happy to answer any of your questions and give you a free consultation on how you can utilize this service to bring affordable fitness to your residents, while creating a revenue stream for you or your homeowners association.
• 我們很樂意回答任何問題並免費提供諮詢:如何有效利用此服務以帶給住戶能負擔的健身運動, 且同時創造收益給你或社區管理委員會。
• For more Information, please:
• visit our website at:
• call:
• Email:
• 更多資訊請:
• 拜訪我們的網站:
• 電話聯絡:
• 傳送電子郵件:
• Quentin Hale
• Marisol Tevet
• Vero Pulse Fitness
• Manager of Marketing and English Translation
• Ph: +17605550187
• LINE ID: driftingotter
• Email: drifting-otter@mailvoro.com
Nice to have
• I would like it to be have a high tech artsy feel. I don't want the haredline industrial.

```html
<!DOCTYPE html>
<html lang="en">
<head>
<meta charset="utf-8">
<title>Vero Pulse Machine Brochure</title>
<link href="https://fonts.googleapis.com/css2?family=Lato:ital,wght@0,400;0,700;0,900;1,700;1,900&family=Noto+Sans+TC:wght@400;700&display=swap" rel="stylesheet">
<style>
:root{
  --ink:#1f1f21;
  --band:#262628;
  --yellow:#e3df3a;
  --yellow-text:#f0e83a;
  --paper:#f4f4f6;
  --stage:#2b2b2d;
  --ring:#3a3a3c;
}
*{box-sizing:border-box;margin:0;padding:0}
html,body{width:1200px;height:789px;overflow:hidden;background:var(--stage)}
body{font-family:"Lato","Noto Sans TC",sans-serif;color:var(--ink)}
.spread{position:absolute;left:40px;top:14px;width:1120px;height:760px;display:flex;box-shadow:0 10px 30px rgba(0,0,0,.5)}
.page{position:relative;width:560px;height:760px;background:var(--paper);overflow:hidden}
.page--left{border-right:1px solid #d6d6da}
.zh{font-family:"Noto Sans TC",sans-serif;font-style:normal}
.en{font-style:italic;font-weight:700}
.abs{position:absolute}
.shape{position:absolute;left:0;top:0}

/* left page */
.intro{left:36px;top:34px;width:490px;color:var(--yellow-text);font-size:12.5px;line-height:1.32}
.intro .zh{display:block;margin-top:10px;font-size:11.5px;line-height:1.45;font-weight:400}
.coin-photo{left:26px;top:210px;width:190px;height:190px;border-radius:50%;border:9px solid var(--ring);background:radial-gradient(circle at 60% 45%,#e8d64a,#c9b22e 60%,#8a7a26)}
.tech{left:236px;top:300px;width:290px;font-size:11.5px;line-height:1.35}
.tech .zh{display:block;margin-top:8px;font-size:10.5px;line-height:1.5}
.payout{left:36px;top:418px;width:490px;font-size:12px;line-height:1.33}
.payout .zh{display:block;margin-top:4px;font-size:11px}
.easy{left:36px;top:510px;width:490px;display:flex;gap:22px;color:var(--yellow-text);font-size:11.5px;line-height:1.35}
.easy ol{list-style:none}
.easy .col-en{width:250px}
.easy .col-zh{width:210px;font-size:11.5px;line-height:1.6}
.tagline{left:36px;top:690px;width:490px;display:flex;justify-content:space-between;font-size:15px;font-weight:900;font-style:italic}
.tagline .zh{font-weight:700;font-size:15px}

/* right page */
.step-label{font-weight:900;font-style:italic;font-size:11px;display:block;margin-bottom:3px}
.step1{left:34px;top:30px;width:300px;font-size:11.5px;line-height:1.35}
.step1 ol{list-style:none;margin:6px 0 4px 8px}
.step1-zh{left:350px;top:44px;width:180px;font-size:10.5px;line-height:1.45}
.meeting{left:34px;top:222px;width:490px;font-size:11.5px;line-height:1.35}
.meeting .zh{display:block;margin-top:3px;font-size:10.5px}
.step2{left:34px;top:298px;width:270px;font-size:11.5px;line-height:1.35}
.step2-zh{left:330px;top:310px;width:190px;font-size:11px;line-height:1.5}
.step3{left:34px;top:382px;width:270px;color:var(--yellow-text);font-size:11.5px;line-height:1.35}
.step3-zh{left:330px;top:396px;width:190px;color:var(--yellow-text);font-size:11px;line-height:1.5}
.photo-strip{left:24px;top:470px;width:512px;height:116px;display:flex;gap:8px}
.photo{flex:1;border:4px solid #5a5a5c}
.photo--coin{background:linear-gradient(135deg,#d8c63a,#b9a52c 60%,#6b6a3a)}
.photo--box{background:linear-gradient(135deg,#e2e2e4,#a9a9ad 55%,#5a5a5e)}
.photo--room{background:linear-gradient(135deg,#d9d45a,#8f8a48 50%,#3a3a40)}
.closing{left:34px;top:612px;width:490px;font-size:11.5px;line-height:1.38}
.closing .zh{display:block;margin-top:6px;font-size:10.5px;line-height:1.5}
</style>
</head>
<body>
<main class="spread" aria-label="Vero Pulse Machine Brochure">

  <section class="page page--left">
    <svg class="shape" width="560" height="760" viewBox="0 0 560 760" aria-hidden="true">
      <path d="M0 0H560V300C470 250 330 240 230 262C150 280 70 290 0 300Z" fill="var(--band)"/>
      <path d="M0 404C180 398 380 410 560 440V505C380 480 180 476 0 482Z" fill="var(--yellow)"/>
      <path d="M0 482C180 476 380 480 560 505V660C380 640 180 640 0 646Z" fill="var(--band)"/>
    </svg>

    <p class="abs intro"><span class="en">We supply cardio equipment to your residents at no cost to you. In fact, we will pay you! Please take a moment to look at our brochure and see how we can work with you and your homeowners association to bring the latest in fitness technology to your building, and we'll pay you for it.</span>
      <span class="zh">在不花費你任何金錢的情況下，我們提供有氧器材給你的住戶。甚至我們付你錢！請看我們的手冊來了解我們如何能和你跟社區管理委員會合作，把最新的健身器材介紹到你的大樓，並且帶給你收益。</span></p>

    <div class="abs coin-photo" role="img" aria-label="Hand inserting a bill into the yellow coin timer on a machine"></div>

    <p class="abs tech"><span class="en">Our machines are all equipped with patented coin operated technology. If your residents would like to have the luxury of quality exercise, they may insert dollars for minutes.</span>
      <span class="zh">我們的器材皆具備專利通過投幣式設計。如果你的住戶想要享有高品質運動，他們可以投幣來取得運動時間。</span></p>

    <p class="abs payout"><span class="en">By the 10th of every month, we will pay 15% of all revenue collected for the previous month, minus taxes, to you or your homeowners association, whichever you choose.</span>
      <span class="zh">每個月10號，我們將付你或社區管理委員會前一個月百分之十五不含稅的收入。</span></p>

    <div class="abs easy">
      <div class="col-en en">
        <p>Why it is so easy:</p>
        <ol>
          <li>1. We provide the equipment at no cost to you.</li>
          <li>2. We pay for shipping and installation.</li>
          <li>3. Month-to-month agreement, no commitment from you.</li>
          <li>4. Removal with 30 days notice, no questions asked.</li>
          <li>5. We conduct all repairs and regular maintenance.</li>
          <li>6. We will pay you from the revenue collected!</li>
        </ol>
      </div>
      <div class="col-zh zh">
        <p>為什麼超簡單：</p>
        <ol>
          <li>1. 不花你一毛錢，器材我們提供。</li>
          <li>2. 運送費跟安裝費，全數我們支付。</li>
          <li>3. 以一個月為一期，不用長期保證。</li>
          <li>4. 30天移出通知，不需任何理由。</li>
          <li>5. 所有器材維修，我們負責。</li>
          <li>6. 器材收益，我們分享！</li>
        </ol>
      </div>
    </div>

    <p class="abs tagline"><span>As easy as 1, 2, 3!</span><span class="zh">簡單有如1, 2, 3!</span></p>
  </section>

  <section class="page page--right">
    <svg class="shape" width="560" height="760" viewBox="0 0 560 760" aria-hidden="true">
      <path d="M0 284L560 300V370L0 362Z" fill="var(--yellow)"/>
      <path d="M0 362L560 370V452L0 446Z" fill="var(--band)"/>
    </svg>

    <div class="abs step1 en">
      <span class="step-label">STEP 1</span>
      <p>We have several different machine types that will motivate your residents to exercise:</p>
      <ol>
        <li>1. Treadmill (photo and stats.)</li>
        <li>2. Recumbent Bike (photo and stats.)</li>
        <li>3. Regular Seated Bike (photo and stats.)</li>
        <li>4. Elliptical trainer (photo and stats.)</li>
      </ol>
      <p>Replace old equipment, broken equipment, or just place new equipment next to your old equipment.</p>
    </div>
    <div class="abs step1-zh zh">
      <p>第一步</p>
      <p>我們有多種有氧器材可讓住戶更有動力運動：</p>
      <p>1. 跑步機<br>2. 臥式腳踏車<br>3. 直立式腳踏車<br>4. 橢圓機</p>
      <p>替換原有老舊的運動器材，或是直接放一台新的器材在原有器材的旁邊。</p>
    </div>

    <p class="abs meeting"><span class="en">After meeting with you and determining you and your residents needs, we will decide how many and of what types of equipment you would like in your exercise room.</span>
      <span class="zh">在和你會面並且評估你和住戶的需求後，我們會決定你想要的器材種類和數量。</span></p>

    <div class="abs step2 en"><span class="step-label">STEP 2</span>We will deliver and install the equipment, in a suitable location that you choose. All at no cost to you!</div>
    <p class="abs step2-zh zh">第二步<br>我們將器材運送到你選擇的合適場所並安裝。不需任何費用！</p>

    <div class="abs step3 en"><span class="step-label">Step 3</span>Make your residents healthy and happy by letting them use any of the equipment, for as long as they like, at their leisure.</div>
    <p class="abs step3-zh zh">第三步<br>住戶可盡情使用任何器材，讓住戶健康又開心。</p>

    <div class="abs photo-strip">
      <div class="photo photo--coin" role="img" aria-label="Step photo: inserting a bill into the coin timer"></div>
      <div class="photo photo--box" role="img" aria-label="Step photo: coins collected in the timer box"></div>
      <div class="photo photo--room" role="img" aria-label="Step photo: residents exercising on treadmills"></div>
    </div>

    <p class="abs closing"><span class="en">We would be happy to answer any of your questions and give you a free consultation on how you can utilize this service to bring affordable fitness to your residents, while creating a revenue stream for you or your homeowners association.</span>
      <span class="zh">我們很樂意回答任何問題並免費提供諮詢：如何有效利用此服務以帶給住戶能負擔的健身運動，且同時創造收益給你或社區管理委員會。</span></p>
  </section>

</main>
</body>
</html>
```